Website homepage rework for women's travel website

I have a homepage (http://www.ladies-far-afield.com) that I'm 50% happy with but don't want to completely overhaul. I'd like to retain a similar look but upgrade it to something a bit more modern and less old-fashioned. The basic sense of the site is empowering, self-confident, fun and adventurous - but female and over 40.

A number of the elements on the page have to be redesigned, a few can be tweaked, and a few left alone. See the rest of the brief for further information.

Target Market(s)

women over 40 who like to travel

Industry/Entity Type

Travel

Number of Pages Required

1 page

Font styles to use
Other font styles liked:
• see my brief

Requirements
Must have
• - size - the page must be significantly wider
• - the only font I MUST keep is Raleway (as in the tagline) and possibly the font of the site name (Ladies Far Afield). Both of those work for me. There are too many fonts on the page, however, and that needs to be unified.
• - the rectangles I click to get inside the site have to change to something more modern, possibly square - they do not have to be separated into two columns as they are now, nor do they need the titles (toolkit etc)
• - I like the background image of the header - but it needs to be wider of course - also keep in mind the aspect - it has to fit into the smaller inside pages, whose size will not change
• - at the end of the project I need to receive the separate elements of the design so I can eventually make a change myself if needed ie. replace my own photo, for example
Nice to have
• - the three photos need to change to something more eye-popping - or something else should take their place to fill the space
Should not have
• I do not want a full, original redesign. I want my readers to still feel as though they are on the same site - same header, mostly same fonts.

```html
<!DOCTYPE html>
<html lang="en">
<head>
<meta charset="utf-8">
<title>Ladies Far Afield – For women who travel smart, safe + solo</title>
<link rel="stylesheet" href="https://fonts.googleapis.com/css2?family=Bebas+Neue&family=Noto+Serif&family=Playfair+Display:ital@1&family=Raleway:wght@400;600&display=swap">
<style>
  :root {
    --ink: #2e2a2b;
    --nav-text: #f5a12a;
    --accent: #f08a1c;
    --body-text: #333;
    --tile-gray: #f4f4f4;
    --search-red: #d8250f;
    --eat: #f04a1a;
    --pack: #a05cc0;
    --stress: #1b9b0c;
    --argentina: #efd60d;
    --supplement: #e8841f;
    --solo: #d0121a;
    --carouge: #3aa8f0;
    --foodies: #3ddbc8;
  }
  * { margin: 0; padding: 0; box-sizing: border-box; }
  html, body { width: 1138px; height: 1200px; overflow: hidden; background: #fff; }
  body { font-family: "Raleway", sans-serif; color: var(--body-text); position: relative; }

  .site-nav {
    height: 53px; background: var(--ink);
    display: flex; justify-content: center; align-items: center; gap: 47px;
  }
  .site-nav a { color: var(--nav-text); text-decoration: none; font-size: 14px; letter-spacing: .2px; }

  .hero {
    position: relative; height: 416px; overflow: hidden;
    background: linear-gradient(180deg, #f6a11a 0%, #f8c42a 35%, #e8a43a 60%, #b7702f 80%, #8a5a36 100%);
  }
  .hero-backdrop {
    position: absolute; inset: 0;
    background: radial-gradient(ellipse at 70% 20%, rgba(255,240,120,.55), transparent 60%),
                linear-gradient(180deg, transparent 55%, rgba(150,60,20,.35) 75%, rgba(80,60,60,.4) 100%);
  }
  .hero-portrait {
    position: absolute; left: 76px; top: 80px; width: 390px; height: 336px;
    background: linear-gradient(180deg, #eeddc0 0%, #d8c6a8 50%, #b8c0b6 100%);
    border-radius: 160px 160px 0 0; opacity: .9;
  }
  .brand {
    position: absolute; left: 513px; top: 84px; width: 465px; height: 58px;
    display: flex; align-items: center; justify-content: center;
  }
  .brand h1 {
    font-family: "Raleway", sans-serif; font-weight: 600; font-style: normal;
    font-size: 44px; color: var(--ink); white-space: nowrap; line-height: 1;
  }
  .tagline {
    position: absolute; left: 513px; top: 146px; width: 465px; text-align: center;
    font-size: 24px; color: #3a2a20; padding: 2px 0 4px;
  }
  .snapshot {
    position: absolute; top: 200px; width: 126px; height: 132px;
    background: #fff; padding: 8px 8px 30px; box-shadow: 0 2px 6px rgba(0,0,0,.3);
  }
  .snapshot span { display: block; width: 100%; height: 100%; }
  .snap-1 { left: 556px; top: 206px; transform: rotate(-4deg); }
  .snap-1 span { background: linear-gradient(180deg, #5fb4e8, #2a7fb0 60%, #3a5a3a); }
  .snap-2 { left: 683px; top: 212px; transform: rotate(2deg); }
  .snap-2 span { background: linear-gradient(180deg, #e8a070, #4aa0d0 55%, #5a8a40); }
  .snap-3 { left: 813px; top: 202px; transform: rotate(-2deg); }
  .snap-3 span { background: linear-gradient(180deg, #c87060, #7aa060 55%, #9a9a90); }

  .hero-notch { position: absolute; left: 0; top: 468px; display: block; }

  .intro { position: absolute; top: 536px; left: 0; width: 1138px; text-align: center; }
  .intro h2 {
    font-family: "Playfair Display", serif; font-style: italic; font-weight: 400;
    font-size: 34px; color: var(--accent); line-height: 1.1;
  }
  .intro p { font-size: 15px; margin-top: 6px; }
  .benefits { list-style: none; text-align: left; width: 520px; margin: 16px 0 0 316px; }
  .benefits li { font-size: 15px; line-height: 25px; display: flex; align-items: center; gap: 10px; }
  .benefits strong { font-weight: 600; color: #222; }

  .cta-band {
    position: absolute; top: 727px; left: 0; width: 1138px; height: 65px; background: var(--ink);
    display: flex; align-items: center; justify-content: center;
    font-family: "Playfair Display", serif; font-style: italic; font-size: 33px; color: var(--accent);
  }
  .cta-band a { color: var(--accent); text-decoration: underline; text-underline-offset: 4px; margin: 0 10px; }

  .topic-grid {
    position: absolute; top: 851px; left: 84px;
    display: grid; grid-template-columns: repeat(3, 320px); grid-auto-rows: 93px; gap: 4px;
  }
  .topic { display: flex; flex-direction: column; text-decoration: none; color: #fff; overflow: hidden; }
  .topic-head { height: 59px; padding: 6px 14px 0; }
  .topic-title { font-family: "Bebas Neue", sans-serif; font-size: 30px; line-height: 28px; display: block; }
  .topic-sub { font-size: 18px; line-height: 20px; display: block; white-space: nowrap; }
  .topic-sub.serif { font-family: "Noto Serif", serif; font-size: 17px; }
  .topic-photo { flex: 1; }

  .t-eat .topic-head { background: var(--eat); }
  .t-eat .topic-photo { background: linear-gradient(90deg, #e8e0d8, #f0a070, #e8e0d8); }
  .t-pack .topic-head { background: var(--pack); }
  .t-pack .topic-photo { background: linear-gradient(90deg, #3a4a7a, #5a6a9a, #d86a5a); }
  .t-stress .topic-head { background: var(--stress); }
  .t-stress .topic-photo { background: linear-gradient(90deg, #e81010, #c01a10, #f02020); }
  .t-arg .topic-head { background: var(--argentina); }
  .t-arg .topic-photo { background: linear-gradient(90deg, #3ac0c8, #7a7060, #3ac0c8); }
  .t-supp .topic-head { background: var(--supplement); }
  .t-supp .topic-photo { background: linear-gradient(180deg, #e8a040, #3a3020); }
  .t-solo .topic-head { background: var(--solo); }
  .t-solo .topic-photo { background: linear-gradient(90deg, #bcd8f0, #f0e0c0, #f8d0c0); }
  .t-car .topic-head { background: var(--carouge); }
  .t-car .topic-photo { background: linear-gradient(90deg, #6a5040, #e83040, #c8a070); }
  .t-food .topic-head { background: var(--foodies); }
  .t-food .topic-photo { background: linear-gradient(90deg, #e8e8e0, #f8c020, #e8e8e0); }

  .search-tile { background: var(--tile-gray); display: flex; align-items: center; padding-left: 30px; }
  .search-box { display: flex; height: 38px; width: 257px; }
  .search-input {
    flex: 1; border: 1px solid #ddd; border-right: none; background: #fff;
    font-family: "Raleway", sans-serif; font-size: 11px; color: #777; display: flex; align-items: center; padding-left: 10px;
  }
  .search-button { width: 40px; background: var(--search-red); display: flex; align-items: center; justify-content: center; }
</style>
</head>
<body>
  <nav class="site-nav">
    <a href="#">START HERE</a>
    <a href="#">ABOUT</a>
    <a href="#">TRAVEL RESOURCES</a>
    <a href="#">BLOG</a>
    <a href="#">TRAVEL SHOP</a>
    <a href="#">CONTACT</a>
  </nav>

  <header class="hero">
    <div class="hero-backdrop" role="img" aria-label="Desert road through red rock buttes under a golden sky with a faded map overlay"></div>
    <div class="hero-portrait" role="img" aria-label="Portrait of the site author smiling, sunglasses on her head"></div>
    <div class="brand"><h1>Ladies Far Afield</h1></div>
    <p class="tagline">For women who travel smart, safe + solo</p>
    <div class="snapshot snap-1"><span role="img" aria-label="Tropical beach with palm trees"></span></div>
    <div class="snapshot snap-2"><span role="img" aria-label="Blue plant pots against an adobe wall"></span></div>
    <div class="snapshot snap-3"><span role="img" aria-label="Red scooter parked on a colourful street"></span></div>
  </header>

  <svg class="hero-notch" width="1138" height="40" viewBox="0 0 1138 40" aria-hidden="true">
    <path d="M450 0 C490 0 500 12 520 24 C545 38 593 38 618 24 C638 12 648 0 688 0 Z" fill="#8a5a36"/>
  </svg>

  <section class="intro">
    <h2>Hi, I’m Marta</h2>
    <p>I took my first solo trip at 15. I’ll show you how to travel…</p>
    <ul class="benefits">
      <li><svg width="16" height="12" viewBox="0 0 16 12"><path d="M1 6 L6 10 L15 1" stroke="var(--accent)" stroke-width="2.5" fill="none"/></svg><span><strong>Smart</strong>: practical tools to help you plan – and afford – the perfect trip</span></li>
      <li><svg width="16" height="12" viewBox="0 0 16 12"><path d="M1 6 L6 10 L15 1" stroke="var(--accent)" stroke-width="2.5" fill="none"/></svg><span><strong>Safe</strong>: down-to-earth advice and a ton of safety recommendations</span></li>
      <li><svg width="16" height="12" viewBox="0 0 16 12"><path d="M1 6 L6 10 L15 1" stroke="var(--accent)" stroke-width="2.5" fill="none"/></svg><span><strong>Solo</strong>: yes, you can do it!</span></li>
    </ul>
  </section>

  <div class="cta-band">Thinking of solo travel? <a href="#">Click here</a> to find out how.</div>

  <main class="topic-grid">
    <a class="topic t-eat" href="#"><div class="topic-head"><span class="topic-title">Eating with Locals</span><span class="topic-sub">The ultimate guide to social dining</span></div><div class="topic-photo" role="img" aria-label="Plated home-cooked dish"></div></a>
    <a class="topic t-pack" href="#"><div class="topic-head"><span class="topic-title">Your Packing List</span><span class="topic-sub serif">Take what you need - no more</span></div><div class="topic-photo" role="img" aria-label="Open suitcase with sandals"></div></a>
    <div class="search-tile">
      <div class="search-box">
        <div class="search-input">Custom Search</div>
        <div class="search-button"><svg width="14" height="14" viewBox="0 0 14 14"><circle cx="6" cy="6" r="4.5" stroke="#fff" stroke-width="1.5" fill="none"/><path d="M9.5 9.5 L13 13" stroke="#fff" stroke-width="1.5"/></svg></div>
      </div>
    </div>
    <a class="topic t-stress" href="#"><div class="topic-head"><span class="topic-title">Stress Management Course</span><span class="topic-sub">How to travel stress-free</span></div><div class="topic-photo" role="img" aria-label="Bold red graphic burst"></div></a>
    <a class="topic t-arg" href="#"><div class="topic-head"><span class="topic-title">Solo in Argentina</span><span class="topic-sub">Does it really take two to tango?</span></div><div class="topic-photo" role="img" aria-label="Steel tower against turquoise sky"></div></a>
    <a class="topic t-supp" href="#"><div class="topic-head"><span class="topic-title">No Single Supplement</span><span class="topic-sub serif">17 ways to avoid paying it</span></div><div class="topic-photo" role="img" aria-label="Sunset over the savanna"></div></a>
    <a class="topic t-solo" href="#"><div class="topic-head"><span class="topic-title">Solo Female Travel</span><span class="topic-sub">A 3-week Central Asia itinerary</span></div><div class="topic-photo" role="img" aria-label="Map of Central Asia"></div></a>
    <a class="topic t-car" href="#"><div class="topic-head"><span class="topic-title">Rebellious Carouge</span><span class="topic-sub">Geneva’s Alter Ego?</span></div><div class="topic-photo" role="img" aria-label="Café terrace with red umbrellas"></div></a>
    <a class="topic t-food" href="#"><div class="topic-head"><span class="topic-title">Europe for Foodies</span><span class="topic-sub">9 top destinations to try in October</span></div><div class="topic-photo" role="img" aria-label="Plate of saffron risotto"></div></a>
  </main>
</body>
</html>
```